TRIVEL Corp Has New Logo Now Needs New Stationary

We just chose our new logo, and now we need a letterhead and envelope design. I would like both to be used via Microsoft Word so I can print both the letterhead and envelopes myself rather than having to the letterhead and envelopes produced by a printing firm. I has attached the new logo and spec sheet provided by the logo designer.

```html
<!DOCTYPE html>
<html lang="en">
<head>
<meta charset="utf-8">
<title>TRIVEL Corp Stationery</title>
<link rel="stylesheet" href="https://fonts.googleapis.com/css2?family=Montserrat:wght@800&display=swap">
<style>
  :root {
    --backdrop: #d3d3d3;
    --paper: #ffffff;
    --leaf: #8cc152;
    --forest: #2d5a27;
    --grass: #3a9a44;
    --sky: #3fa9e0;
    --ocean: #1f6fb5;
    --ink: #2b2b2b;
  }
  * { box-sizing: border-box; margin: 0; padding: 0; }
  html, body { width: 1200px; height: 813px; overflow: hidden; }
  body {
    background: var(--backdrop);
    font-family: "Montserrat", Arial, sans-serif;
    position: relative;
  }
  .sheet {
    position: absolute;
    background: var(--paper);
    box-shadow: 0 2px 6px rgba(0,0,0,0.12);
    overflow: hidden;
  }
  .letterhead { left: 640px; top: 64px; width: 480px; height: 680px; }
  .envelope { left: 80px; top: 430px; width: 480px; height: 240px; }

  .decor-corner {
    position: absolute;
    background: linear-gradient(90deg, var(--forest) 0%, var(--forest) 55%, var(--leaf) 100%);
  }
  .letterhead .decor-corner.top-left { left: 0; top: 0; width: 80px; height: 210px; }
  .letterhead .decor-corner.bottom-right {
    right: 0; bottom: 0; width: 80px; height: 210px;
    background: linear-gradient(270deg, var(--forest) 0%, var(--forest) 55%, var(--leaf) 100%);
  }
  .envelope .decor-corner.top-left { left: 0; top: 0; width: 64px; height: 84px; }

  .decor-swoosh {
    position: absolute;
    background: linear-gradient(180deg, rgba(140,193,82,0) 0%, rgba(140,193,82,0.55) 45%, rgba(31,111,181,0.55) 100%);
  }
  .letterhead .decor-swoosh { left: 8px; bottom: 0; width: 362px; height: 62px; }
  .envelope .decor-swoosh { left: 14px; bottom: 0; width: 366px; height: 96px;
    background: linear-gradient(180deg, rgba(63,169,224,0) 0%, rgba(63,169,224,0.35) 45%, rgba(140,193,82,0.5) 100%);
  }

  .rule {
    position: absolute;
    height: 6px;
    background: var(--sky);
  }
  .rule-top { right: 10px; top: 92px; width: 180px; }
  .rule-bottom { left: 28px; top: 480px; width: 170px; }

  .brand {
    position: absolute;
    display: flex;
    align-items: center;
    gap: 6px;
    color: var(--ink);
    font-weight: 800;
    letter-spacing: 0.04em;
    white-space: nowrap;
  }
  .brand-dot { border-radius: 50%; background: var(--grass); flex: none; }
  .letterhead .brand { right: 22px; top: 60px; font-size: 12px; }
  .letterhead .brand-dot { width: 10px; height: 10px; }
  .envelope .brand { left: 232px; top: 96px; font-size: 22px; }
  .envelope .brand-dot { width: 18px; height: 18px; }

  .field-label {
    position: absolute;
    color: var(--ink);
    font-weight: 800;
    font-size: 10px;
    letter-spacing: 0.06em;
  }
  .field-sender { left: 92px; top: 34px; }
  .field-address { left: 62px; top: 104px; }
</style>
</head>
<body>

<section class="sheet letterhead" aria-label="Letterhead">
  <div class="decor-corner top-left" role="img" aria-label="Green and blue wave ornament in the top left corner"></div>
  <div class="decor-corner bottom-right" role="img" aria-label="Green and blue wave ornament in the bottom right corner"></div>
  <div class="decor-swoosh" role="img" aria-label="Green and blue swoosh ornament along the bottom edge"></div>
  <div class="rule rule-top"></div>
  <div class="rule rule-bottom"></div>
  <div class="brand"><span class="brand-dot"></span>TRIVEL CORP</div>
</section>

<section class="sheet envelope" aria-label="Envelope">
  <div class="decor-corner top-left" role="img" aria-label="Green and blue wave ornament in the top left corner"></div>
  <div class="decor-swoosh" role="img" aria-label="Flowing blue lines and green swoosh ornament along the bottom"></div>
  <div class="field-label field-sender">YOUR TEXT</div>
  <div class="field-label field-address">YOUR ADDRESS</div>
  <div class="brand"><span class="brand-dot"></span>TRIVEL CORP</div>
</section>

</body>
</html>
```